Website To Serve As A Resource For Medical Conditions

I need a website that is attractive that will be utilized to educate patients on either hepatitis c or HIV so it should be easily readable attractive but also professional. This website is going to be furnished with various topics for example, HIV treatment, HIV and Nutrition, HIV and Exercise, HIV and....

This website will also be cloned and utilized similarly for Hepatitis.

Coded - Design and coding required

1 page

0094D4
00A9DD
6FCCEA
C7EBF8
E9F6FB
A7469A
B969AE
D3A5CF
EDDBEB
F8F0F9
6B429C
8869AF
B7A5CE
E3DAEB
F3F0F8

```html
<!DOCTYPE html>
<html lang="en">
<head>
<meta charset="utf-8">
<title>HIV Conditions</title>
<link rel="stylesheet" href="https://fonts.googleapis.com/css2?family=Roboto+Slab:wght@500;600;700&family=Montserrat:wght@400;500;600&family=Roboto+Condensed:wght@700&family=Roboto:wght@500;700&display=swap">
<style>
:root{
  --blue:#0094d4;
  --blue-light:#00a9dd;
  --purple:#a7469a;
  --purple-soft:#b969ae;
  --ink:#2a3340;
  --text:#3b3f47;
  --white:#ffffff;
  --footer:#17202e;
  --footer-text:#c9ced8;
  --star:#f7b500;
}
*{box-sizing:border-box;margin:0;padding:0}
html,body{width:1200px;height:4080px;overflow:hidden}
body{position:relative;background:var(--white);font-family:"Montserrat",sans-serif;color:var(--text)}
.abs{position:absolute}
h1,h2,.logo{font-family:"Roboto Slab",serif}
.btn{position:absolute;display:flex;align-items:center;justify-content:center;gap:14px;background:var(--blue);color:var(--white);font-family:"Roboto",sans-serif;font-weight:700;font-size:15px;letter-spacing:.2px;text-transform:uppercase;height:46px;border-radius:2px}
.btn svg{width:20px;height:20px}
.eyebrow{position:absolute;font-family:"Roboto Slab",serif;font-weight:600;font-size:16px;color:var(--purple)}
.title{position:absolute;font-family:"Roboto Slab",serif;font-weight:600;font-size:35px;color:var(--ink);line-height:1}
.para{position:absolute;font-size:15px;line-height:24.7px;color:var(--text)}
.centered{left:0;width:1200px;text-align:center}

/* header & hero */
.hero-band{left:0;top:0;width:910px;height:644px;background:var(--purple)}
.topbar-white{left:910px;top:0;width:290px;height:130px;background:var(--white)}
.logo{position:absolute;left:35px;top:12px;font-size:35px;font-weight:600;color:var(--white)}
.nav{position:absolute;top:24px;left:0;font-family:"Roboto Condensed",sans-serif;font-weight:700;font-size:13px;color:var(--white)}
.nav span{position:absolute;white-space:nowrap}
.nav .active::before{content:"";position:absolute;left:50%;top:-10px;width:4px;height:4px;margin-left:-2px;border-radius:50%;background:var(--white)}
.phone{position:absolute;left:946px;top:21px;display:flex;align-items:center;gap:6px;font-size:14px;font-weight:500;color:var(--purple)}
.hero-photo{left:612px;top:130px;width:588px;height:646px;background:linear-gradient(160deg,#d9dde3 0%,#c4ccd6 40%,#e8eaee 70%,#b6c0cc 100%)}
.hero-title{position:absolute;left:109px;top:240px;font-size:54px;font-weight:700;color:var(--white);line-height:1.1}
.hero-sub{position:absolute;left:109px;top:314px;width:470px;font-size:19.5px;font-weight:500;line-height:30px;color:var(--white)}
.slider-nav{left:484px;top:649px;width:127px;height:57px;background:var(--white);box-shadow:0 6px 14px rgba(0,0,0,.12);display:flex;align-items:center;justify-content:center;gap:36px}

/* about */
.about-photo{left:673px;top:861px;width:416px;height:394px;background:linear-gradient(135deg,#8a5a44 0%,#c9917a 45%,#e9d6cc 75%,#b97d66 100%)}
.badge{left:635px;top:1127px;width:188px;height:163px;background:var(--purple);box-shadow:0 6px 14px rgba(0,0,0,.2);color:var(--white);text-align:center;font-family:"Roboto Slab",serif}
.badge .num{font-size:62px;font-weight:600;margin-top:14px;line-height:1.1}
.badge .yrs{font-size:24px;font-weight:600;letter-spacing:5px}

/* treatment */
.treatment-band{left:0;top:1377px;width:1200px;height:583px;background:var(--blue)}
.card{position:absolute;background:var(--white);border-radius:8px;box-shadow:0 6px 18px rgba(0,0,0,.15)}
.card h3{position:absolute;left:28px;font-family:"Montserrat",sans-serif;font-weight:600;font-size:22.5px;color:var(--ink)}
.card p{position:absolute;left:28px;width:250px;font-size:14px;line-height:24.3px;color:#555b66}
.tcard{top:1550px;width:310px;height:326px}
.tcard .icon{position:absolute;left:28px;top:36px;width:78px;height:76px}
.tcard h3{top:131px}
.tcard p{top:168px}
.tcard .stars{position:absolute;left:28px;top:286px;display:flex;gap:3px}
.circle-arrow{width:60px;height:60px;border:2px solid var(--white);border-radius:50%;display:flex;align-items:center;justify-content:center}

/* nutrition */
.nutri-frame{left:119px;top:2050px;width:414px;height:391px;border:9px solid var(--purple)}
.nutri-photo{position:absolute;left:8px;top:8px;right:8px;bottom:8px;background:linear-gradient(110deg,#eef0f2 0%,#d6d9dd 45%,#7b6a5f 70%,#c8ccd2 100%)}

/* exercise */
.exercise-band{left:0;top:2528px;width:1200px;height:778px;background:var(--purple)}
.ecard{top:2707px;width:310px;height:450px}
.ecard .photo{position:absolute;left:11px;top:11px;width:288px;height:244px;border-radius:6px}
.ecard .tag{position:absolute;left:28px;top:270px;font-size:15px;font-weight:600;color:var(--blue)}
.ecard h3{top:289px}
.ecard p{top:330px}

/* footer */
.footer{left:0;top:3673px;width:1200px;height:407px;background:var(--footer)}
.f-logo{position:absolute;left:209px;top:3806px;font-size:34px;font-weight:600;color:var(--white)}
.f-desc{position:absolute;left:192px;top:3862px;width:290px;font-size:12.5px;line-height:20px;color:var(--white)}
.social{position:absolute;top:3953px;width:32px;height:32px;border-radius:50%;background:#2c3a52}
.f-col{position:absolute;top:3765px}
.f-col h4{font-family:"Montserrat",sans-serif;font-weight:600;font-size:17px;color:var(--white);letter-spacing:.3px}
.f-col .rule{width:50px;height:2px;background:var(--blue);margin:13px 0 17px}
.f-col li{list-style:none;font-size:12.5px;color:var(--footer-text);line-height:26.6px}
.f-divider{left:111px;top:4029px;width:978px;height:1px;background:#2e3a4c}
.copyright{position:absolute;left:0;width:1200px;top:4046px;text-align:center;font-size:12.5px;color:var(--footer-text)}
</style>
</head>
<body>

<!-- header & hero -->
<div class="abs hero-band"></div>
<div class="abs topbar-white"></div>
<div class="logo">HIV Conditions</div>
<nav class="nav">
  <span class="active" style="left:337px">Home</span>
  <span style="left:408px">HIV Treatment</span>
  <span style="left:530px">HIV and Nutrition</span>
  <span style="left:668px">HIV and Exercise</span>
  <span style="left:804px">HIV and Others</span>
</nav>
<div class="phone">
  <svg width="18" height="18" viewBox="0 0 24 24" fill="none" stroke="#a7469a" stroke-width="2" stroke-linecap="round" stroke-linejoin="round"><path d="M22 16.9v3a2 2 0 0 1-2.2 2 19.8 19.8 0 0 1-8.6-3.1 19.5 19.5 0 0 1-6-6A19.8 19.8 0 0 1 2.1 4.2 2 2 0 0 1 4.1 2h3a2 2 0 0 1 2 1.7c.1 1 .4 1.9.7 2.8a2 2 0 0 1-.5 2.1L8 9.9a16 16 0 0 0 6 6l1.3-1.3a2 2 0 0 1 2.1-.4c.9.3 1.8.6 2.8.7a2 2 0 0 1 1.7 2z"/></svg>
  +1 555 010 0199
</div>
<div class="btn" style="left:934px;top:60px;width:153px">Contact Us
  <svg viewBox="0 0 20 20"><circle cx="10" cy="10" r="9" fill="#fff"/><path d="M8.5 6l4 4-4 4" fill="none" stroke="#0094d4" stroke-width="2"/></svg></div>

<div class="abs hero-photo" role="img" aria-label="Young man in a white t-shirt holding a red awareness ribbon"></div>
<h1 class="hero-title">HIV Conditions</h1>
<p class="hero-sub">Saers lkses sepiciatis unde omnis istesit volupt atem asccusan tium doloremque.</p>
<div class="btn" style="left:109px;top:393px;width:155px;height:45px">Get Started
  <svg viewBox="0 0 20 20"><circle cx="10" cy="10" r="9" fill="#fff"/><path d="M8.5 6l4 4-4 4" fill="none" stroke="#0094d4" stroke-width="2"/></svg></div>
<div class="abs slider-nav">
  <svg width="14" height="22" viewBox="0 0 14 22"><path d="M11 3L3 11l8 8" fill="none" stroke="#a7469a" stroke-width="2.5"/></svg>
  <svg width="14" height="22" viewBox="0 0 14 22"><path d="M3 3l8 8-8 8" fill="none" stroke="#a7469a" stroke-width="2.5"/></svg>
</div>

<!-- about -->
<div class="eyebrow" style="left:116px;top:859px">About Us</div>
<h2 class="title" style="left:114px;top:882px">HIV Conditions</h2>
<p class="para" style="left:109px;top:930px;width:474px">Saerspiciatis undeasepoiise oklasdo mnis aidaste natus error sit voluptatem accusan tium doloremque laudantium, totam rem aperiam, ease aque ipaefdsa quae ab illo inventore veritatis ease quasi architecto beatae vitae dicta sunt explicabo. Nemo enim ipsam voluptatem quia volasdfupta sde sessitasese aspernatur autodit aut fugitsdsed quisaea consequuntur magni dolores eos qui ratione voluptatem sequi nesciunt.</p>
<p class="para" style="left:109px;top:1117px;width:474px">Nemo enim ipsam voluptatem quia volasdfupta sde sessitasese aspernatur autodit aut fugitsdsed quisaea consequuntur magni dolores eos qui ratione voluptatem sequi nesciunt.</p>
<div class="btn" style="left:109px;top:1216px;width:153px">Learn More
  <svg viewBox="0 0 20 20"><circle cx="10" cy="10" r="9" fill="#fff"/><path d="M8.5 6l4 4-4 4" fill="none" stroke="#0094d4" stroke-width="2"/></svg></div>
<div class="abs about-photo" role="img" aria-label="Circle of open hands each holding a red awareness ribbon"></div>
<div class="abs badge"><div class="num">20+</div><div class="yrs">Years</div></div>

<!-- treatment -->
<div class="abs treatment-band"></div>
<div class="eyebrow centered" style="top:1458px;color:#fff">Treatment</div>
<h2 class="title centered" style="top:1481px;color:#fff">HIV Treatment</h2>
<div class="abs circle-arrow" style="left:40px;top:1689px">
  <svg width="26" height="20" viewBox="0 0 26 20"><path d="M24 10H3M10 3L3 10l7 7" fill="none" stroke="#fff" stroke-width="2.2"/></svg></div>
<div class="abs circle-arrow" style="left:1099px;top:1689px">
  <svg width="26" height="20" viewBox="0 0 26 20"><path d="M2 10h21M16 3l7 7-7 7" fill="none" stroke="#fff" stroke-width="2.2"/></svg></div>

<div class="card tcard" style="left:111px">
  <svg class="icon" viewBox="0 0 78 76" fill="none" stroke="#1f2530" stroke-width="2.4" stroke-linejoin="round" stroke-linecap="round"><path d="M39 36C27 27 22 20 22 13a9 9 0 0 1 17-4 9 9 0 0 1 17 4c0 7-5 14-17 23z" stroke="#0094d4"/><path d="M39 14v12M33 20h12" stroke="#0094d4"/><path d="M6 34l10 16 8 8v16M72 34L62 50l-8 8v16M16 40l8 12M62 40l-8 12"/></svg>
  <h3>Protease Inhibitors</h3>
  <p>Saerspiciatis unde omnis iste natus error sit voluptatem accusan tium doloremque laudantiumotam rem aperiameaque.</p>
  <div class="stars">
    <svg width="20" height="19" viewBox="0 0 20 19"><path d="M10 0l3 6.2 6.8 1-5 4.8 1.2 6.8L10 15.6 4 18.8 5.2 12 .2 7.2l6.8-1z" fill="#f7b500"/></svg>
    <svg width="20" height="19" viewBox="0 0 20 19"><path d="M10 0l3 6.2 6.8 1-5 4.8 1.2 6.8L10 15.6 4 18.8 5.2 12 .2 7.2l6.8-1z" fill="#f7b500"/></svg>
    <svg width="20" height="19" viewBox="0 0 20 19"><path d="M10 0l3 6.2 6.8 1-5 4.8 1.2 6.8L10 15.6 4 18.8 5.2 12 .2 7.2l6.8-1z" fill="#f7b500"/></svg>
    <svg width="20" height="19" viewBox="0 0 20 19"><path d="M10 0l3 6.2 6.8 1-5 4.8 1.2 6.8L10 15.6 4 18.8 5.2 12 .2 7.2l6.8-1z" fill="#f7b500"/></svg>
    <svg width="20" height="19" viewBox="0 0 20 19"><path d="M10 0l3 6.2 6.8 1-5 4.8 1.2 6.8L10 15.6 4 18.8 5.2 12 .2 7.2l6.8-1z" fill="#f7b500"/></svg>
  </div>
</div>
<div class="card tcard" style="left:445px">
  <svg class="icon" viewBox="0 0 78 76" fill="none" stroke="#1f2530" stroke-width="2.4" stroke-linejoin="round" stroke-linecap="round"><path d="M34 10l24-6v68l-24-6z"/><path d="M34 10h30v56H34"/><path d="M2 38h26M20 30l8 8-8 8" stroke="#0094d4"/></svg>
  <h3>Entry Inhibitors</h3>
  <p>Saerspiciatis unde omnis iste natus error sit voluptatem accusan tium doloremque laudantiumotam rem aperiameaque.</p>
  <div class="stars">
    <svg width="20" height="19" viewBox="0 0 20 19"><path d="M10 0l3 6.2 6.8 1-5 4.8 1.2 6.8L10 15.6 4 18.8 5.2 12 .2 7.2l6.8-1z" fill="#f7b500"/></svg>
    <svg width="20" height="19" viewBox="0 0 20 19"><path d="M10 0l3 6.2 6.8 1-5 4.8 1.2 6.8L10 15.6 4 18.8 5.2 12 .2 7.2l6.8-1z" fill="#f7b500"/></svg>
    <svg width="20" height="19" viewBox="0 0 20 19"><path d="M10 0l3 6.2 6.8 1-5 4.8 1.2 6.8L10 15.6 4 18.8 5.2 12 .2 7.2l6.8-1z" fill="#f7b500"/></svg>
    <svg width="20" height="19" viewBox="0 0 20 19"><path d="M10 0l3 6.2 6.8 1-5 4.8 1.2 6.8L10 15.6 4 18.8 5.2 12 .2 7.2l6.8-1z" fill="#f7b500"/></svg>
    <svg width="20" height="19" viewBox="0 0 20 19"><path d="M10 0l3 6.2 6.8 1-5 4.8 1.2 6.8L10 15.6 4 18.8 5.2 12 .2 7.2l6.8-1z" fill="#f7b500"/></svg>
  </div>
</div>
<div class="card tcard" style="left:779px">
  <svg class="icon" viewBox="0 0 78 76" fill="none" stroke="#1f2530" stroke-width="2.4" stroke-linejoin="round" stroke-linecap="round"><path d="M14 62L52 24l8 8-38 38z"/><path d="M56 20l12-12M62 6l8 8M8 68l6-6"/><path d="M24 52l4 4M30 46l4 4M36 40l4 4"/><circle cx="14" cy="24" r="6" stroke="#0094d4"/><circle cx="60" cy="54" r="6" stroke="#0094d4"/><ellipse cx="14" cy="40" rx="6" ry="3.5"/><ellipse cx="48" cy="64" rx="5" ry="3"/><ellipse cx="64" cy="68" rx="4" ry="3"/><circle cx="32" cy="12" r="3"/></svg>
  <h3>Multi-Drug Regimens</h3>
  <p>Saerspiciatis unde omnis iste natus error sit voluptatem accusan tium doloremque laudantiumotam rem aperiameaque.</p>
  <div class="stars">
    <svg width="20" height="19" viewBox="0 0 20 19"><path d="M10 0l3 6.2 6.8 1-5 4.8 1.2 6.8L10 15.6 4 18.8 5.2 12 .2 7.2l6.8-1z" fill="#f7b500"/></svg>
    <svg width="20" height="19" viewBox="0 0 20 19"><path d="M10 0l3 6.2 6.8 1-5 4.8 1.2 6.8L10 15.6 4 18.8 5.2 12 .2 7.2l6.8-1z" fill="#f7b500"/></svg>
    <svg width="20" height="19" viewBox="0 0 20 19"><path d="M10 0l3 6.2 6.8 1-5 4.8 1.2 6.8L10 15.6 4 18.8 5.2 12 .2 7.2l6.8-1z" fill="#f7b500"/></svg>
    <svg width="20" height="19" viewBox="0 0 20 19"><path d="M10 0l3 6.2 6.8 1-5 4.8 1.2 6.8L10 15.6 4 18.8 5.2 12 .2 7.2l6.8-1z" fill="#f7b500"/></svg>
    <svg width="20" height="19" viewBox="0 0 20 19"><path d="M10 0l3 6.2 6.8 1-5 4.8 1.2 6.8L10 15.6 4 18.8 5.2 12 .2 7.2l6.8-1z" fill="#f7b500"/></svg>
  </div>
</div>

<!-- nutrition -->
<div class="abs nutri-frame"><div class="nutri-photo" role="img" aria-label="Patient in bed receiving a tray with a healthy meal"></div></div>
<div class="eyebrow" style="left:614px;top:2050px">Nutrition</div>
<h2 class="title" style="left:613px;top:2079px">HIV and Nutrition</h2>
<p class="para" style="left:614px;top:2130px;width:474px">Saerspiciatis undeasepoiise oklasdo mnis aidaste natus error sit voluptatem accusan tium doloremque laudantium, totam rem aperiam, ease aque ipaefdsa quae ab illo inventore veritatis ease quasi architecto beatae vitae dicta sunt explicabo. Nemo enim ipsam voluptatem quia volasdfupta sde sessitasese aspernatur autodit aut fugitsdsed quisaea consequuntur magni dolores eos qui ratione voluptatem sequi nesciunt.</p>
<p class="para" style="left:614px;top:2317px;width:474px">Nemo enim ipsam voluptatem quia volasdfupta sde sessitasese aspernatur autodit aut fugitsdsed.</p>
<div class="btn" style="left:614px;top:2386px;width:153px">Learn More
  <svg viewBox="0 0 20 20"><circle cx="10" cy="10" r="9" fill="#fff"/><path d="M8.5 6l4 4-4 4" fill="none" stroke="#0094d4" stroke-width="2"/></svg></div>

<!-- exercise -->
<div class="abs exercise-band"></div>
<div class="eyebrow centered" style="top:2612px;color:#fff">Exercise</div>
<h2 class="title centered" style="top:2635px;color:#fff">HIV and Exercise</h2>

<div class="card ecard" style="left:111px">
  <div class="photo" role="img" aria-label="Group of adults stretching together in a bright gym" style="background:linear-gradient(135deg,#cfd8dc 0%,#f1f1f1 40%,#b9a58f 75%,#e3e6ea 100%)"></div>
  <div class="tag">Eancididunt</div>
  <h3>Consectetur Sadipiscin</h3>
  <p>Saerspiciatis unde omnis iste natus error sitvoluptatem accusan tium doloremque laudantiumotam rem aperiameaque.</p>
</div>
<div class="card ecard" style="left:445px">
  <div class="photo" role="img" aria-label="Man meditating cross-legged in a yoga class" style="background:linear-gradient(135deg,#a89a88 0%,#d8cbb8 40%,#6f6b68 70%,#c7b7a2 100%)"></div>
  <div class="tag">Eancididunt</div>
  <h3>Consectetur Sadipiscin</h3>
  <p>Saerspiciatis unde omnis iste natus error sitvoluptatem accusan tium doloremque laudantiumotam rem aperiameaque.</p>
</div>
<div class="card ecard" style="left:779px">
  <div class="photo" role="img" aria-label="Older women doing a group exercise class" style="background:linear-gradient(135deg,#e2dcd4 0%,#c9c0b1 40%,#9aa48a 70%,#ebe6df 100%)"></div>
  <div class="tag">Eancididunt</div>
  <h3>Consectetur Sadipiscin</h3>
  <p>Saerspiciatis unde omnis iste natus error sitvoluptatem accusan tium doloremque laudantiumotam rem aperiameaque.</p>
</div>
<div class="btn" style="left:524px;top:3175px;width:152px">View More
  <svg viewBox="0 0 20 20"><circle cx="10" cy="10" r="9" fill="#fff"/><path d="M8.5 6l4 4-4 4" fill="none" stroke="#0094d4" stroke-width="2"/></svg></div>

<!-- others -->
<div class="eyebrow centered" style="top:3390px">Others</div>
<h2 class="title centered" style="top:3410px">HIV and Others</h2>
<p class="para" style="left:125px;top:3461px;width:950px;text-align:center">Saerspiciatis undeasepoiise oklasdo mnis aidaste natus error sit voluptatem accusan tium doloremque laudantium, totam rem aperiam, ease aque ipaefdsa quae ab illo inventore veritatis ease quasi architecto beatae vitae dicta sunt explicabo. Nemo enim ipsam voluptatem quia volasdfupta sde sessitasese aspernatur autodit.</p>
<div class="btn" style="left:524px;top:3565px;width:152px">Learn More
  <svg viewBox="0 0 20 20"><circle cx="10" cy="10" r="9" fill="#fff"/><path d="M8.5 6l4 4-4 4" fill="none" stroke="#0094d4" stroke-width="2"/></svg></div>

<!-- footer -->
<footer class="abs footer"></footer>
<div class="f-logo logo">HIV Conditions</div>
<p class="f-desc">Saerspiciatis undeassdkj epoiise oklasdo mnis aidaste natus errors sitase voluptatem accusan tium doloremque laudantium.</p>
<div class="social" style="left:275px" aria-label="Social profile"></div>
<div class="social" style="left:321px" aria-label="Social profile"></div>
<div class="f-col" style="left:556px"><h4>QUICK LINKS</h4><div class="rule"></div>
  <ul><li>Home</li><li>HIV Treatment</li><li>HIV and Nutrition</li><li>HIV and Exercise</li><li>HIV and Others</li><li>COntact Us</li></ul></div>
<div class="f-col" style="left:747px"><h4>LINKS</h4><div class="rule"></div>
  <ul><li>Copyright</li><li>Legal</li><li>Privacy</li><li>Accessibility</li><li>Sitemap</li></ul></div>
<div class="f-col" style="left:912px"><h4>SUPPORT</h4><div class="rule"></div>
  <ul><li>Team</li><li>About Us</li><li>Careers</li><li>Our Values</li></ul></div>
<div class="abs f-divider"></div>
<div class="copyright">©2023. All rights reserved.</div>

</body>
</html>
```